Business Card & Stationary
Powder Coating Company
Project: Business Card & Stationary
Business Card & Stationary - Miscellaneous
Creative Brief
Professional
Rutger Vandelow
Owner / Operator
4715 Ave K 1/2
nullemail@brindlecoatfinish.com
www.brindlecoatfinish.com
Should list our services, which include Powder Coating, Ceramic Coating and Abrasive Blasting

```html
<!DOCTYPE html>
<html lang="en">
<head>
<meta charset="utf-8">
<title>Brindlecoat Finish – Business Cards</title>
<link href="https://fonts.googleapis.com/css2?family=Roboto:wght@400;700&display=swap" rel="stylesheet">
<style>
  :root{
    --bg:#ecebe8;
    --paper:#ffffff;
    --red:#e0203a;
    --red-deep:#b5142b;
    --ink:#2b2b2b;
    --grey:#6d6d6d;
    --rule:#d9d9d9;
  }
  *{box-sizing:border-box;margin:0;padding:0}
  html,body{width:1200px;height:646px;overflow:hidden}
  body{background:var(--bg);font-family:"Roboto",Arial,sans-serif;position:relative}

  .card{position:absolute;top:173px;width:520px;height:300px;background:var(--paper);
        box-shadow:0 6px 18px rgba(0,0,0,.18);overflow:hidden}
  .card--front{left:50px}
  .card--back{left:630px}

  .brand{display:flex;align-items:center;gap:10px;color:var(--red);font-weight:700;letter-spacing:.5px;white-space:nowrap}
  .brand__dot{width:12px;height:12px;border-radius:50%;background:var(--red);flex:none}

  .card--front .brand{position:absolute;left:0;right:0;top:104px;justify-content:center;font-size:36px}
  .services{position:absolute;left:0;right:0;top:160px;text-align:center;font-size:12px;
            color:var(--grey);letter-spacing:1px;text-transform:uppercase}
  .card--front .web{position:absolute;left:34px;bottom:30px;font-size:12px;color:var(--ink)}

  .band{position:absolute;inset:0}
  .card--back .brand{position:absolute;left:30px;top:74px;font-size:20px;gap:8px}
  .card--back .brand__dot{width:10px;height:10px}

  .person{position:absolute;left:30px;top:176px}
  .person__name{color:var(--red);font-weight:700;font-size:19px}
  .person__role{color:var(--grey);font-size:12px;margin-top:4px}

  .contact{position:absolute;right:24px;top:58px;list-style:none;color:#fff;font-size:10.5px;text-align:right}
  .contact li{display:flex;justify-content:flex-end;align-items:center;gap:8px;height:22px;white-space:nowrap}
  .contact svg{width:11px;height:11px;fill:#fff;flex:none}
</style>
</head>
<body>

<section class="card card--front" aria-label="Business card front">
  <div class="brand"><span class="brand__dot"></span>Brindlecoat Finish</div>
  <p class="services">Powder Coating · Ceramic Coating · Abrasive Blasting</p>
  <p class="web">www.brindlecoatfinish.com</p>
</section>

<section class="card card--back" aria-label="Business card back">
  <svg class="band" viewBox="0 0 520 300" preserveAspectRatio="none" aria-hidden="true">
    <path d="M325 0 C275 90 355 170 235 300 L520 300 L520 0 Z" fill="var(--red)"/>
    <path d="M317 0 C267 90 347 170 227 300" fill="none" stroke="var(--red-deep)" stroke-width="3"/>
    <path d="M309 0 C259 90 339 170 219 300" fill="none" stroke="var(--rule)" stroke-width="1.5"/>
  </svg>
  <div class="brand"><span class="brand__dot"></span>Brindlecoat Finish</div>
  <div class="person">
    <p class="person__name">Rutger Vandelow</p>
    <p class="person__role">Owner / Operator</p>
  </div>
  <ul class="contact">
    <li>4715 Ave K 1/2<svg viewBox="0 0 10 10"><path d="M5 0a3.5 3.5 0 0 0-3.5 3.5C1.5 6 5 10 5 10s3.5-4 3.5-6.5A3.5 3.5 0 0 0 5 0zm0 5a1.5 1.5 0 1 1 0-3 1.5 1.5 0 0 1 0 3z"/></svg></li>
    <li>(409) 555-0142<svg viewBox="0 0 10 10"><path d="M2 0l2 2.5-1 1.2a6 6 0 0 0 3.3 3.3l1.2-1L10 8 8.6 10C4 9.6.4 6 0 1.4z"/></svg></li>
    <li>(409) 555-0187<svg viewBox="0 0 10 10"><path d="M2 0l2 2.5-1 1.2a6 6 0 0 0 3.3 3.3l1.2-1L10 8 8.6 10C4 9.6.4 6 0 1.4z"/></svg></li>
    <li>nullemail@brindlecoatfinish.com<svg viewBox="0 0 10 10"><path d="M0 2h10v6H0zm1 1v.4l4 2.4 4-2.4V3z"/></svg></li>
    <li>www.brindlecoatfinish.com<svg viewBox="0 0 10 10"><circle cx="5" cy="5" r="4.5" fill="none" stroke="#fff"/><path d="M0.5 5h9M5 .5v9" stroke="#fff" fill="none"/></svg></li>
  </ul>
</section>

</body>
</html>
```